Management consultant needs to update look of website

Currently I have a great word press website but it needs an updated look. I have new text for the site in the attached word document. I also have a list of websites whose design, look, and organization i like as a guide for the designer. The final design should be simple, strong, clear, and project the idea that my brand is a powerful authority in this space. Current site = www.brookfernadvisory.com

Target Market(s)

company owners / executives

Industry/Entity Type

Management Consulting

Number of Pages Required

3 page

Font styles to use
Serif

Colors

Designer to choose colors to be used in the design.

Requirements
Must have
• a simple and clear design and message. professional look. easy navigation. responsive to mobile devices. an easily implemented wordpress theme OR squarespace. use of my logo colors. though I am open to changing to a deep navy or charcoal logo image. source file uploaded.
Nice to have
• i like the cover photo and logo watermark on my current homepage. i like the google map with my logo on the current contact page. i like the animation as well. a great blend of the current site and something that is more seamless.

```html
<!DOCTYPE html>
<html lang="en">
<head>
<meta charset="utf-8">
<title>Brookfern Advisory</title>
<link href="https://fonts.googleapis.com/css2?family=Roboto+Slab:wght@300;400;700&family=Lora:ital@1&display=swap" rel="stylesheet">
<style>
:root{
  --gold:#c79f3c;
  --gold-dark:#b08a2e;
  --ink:#4f4f4f;
  --text:#444;
  --muted:#ececec;
  --footer:#3e3e3e;
  --white:#fff;
}
*{margin:0;padding:0;box-sizing:border-box}
html,body{width:1200px;height:2871px;overflow:hidden;background:var(--white)}
body{position:relative;font-family:"Roboto Slab",Georgia,serif;color:var(--text)}
.abs{position:absolute}
.center{left:0;width:1200px;text-align:center}

/* nav */
.top-line{top:0;left:0;width:1200px;height:4px;background:var(--gold)}
.brand{left:173px;top:16px;display:flex;align-items:center;gap:10px}
.brand-dot{width:48px;height:48px;border-radius:50%;background:var(--gold)}
.brand-name{font-size:19px;color:var(--gold);line-height:1.05}
.brand-name small{display:block;font-size:10px;letter-spacing:.5px}
.nav{top:25px;left:597px;display:flex;gap:0;font-size:13px;color:#333}
.nav a{display:block;padding:8px 12px;margin-right:18px;text-decoration:none;color:#333}
.nav a.active{background:var(--gold);color:var(--white)}

/* hero */
.hero{top:77px;left:0}
.hero-title{top:258px;font-size:44px;color:#2b2b2b;letter-spacing:1px}
.btn-start{top:333px;left:528px;width:144px;height:38px;border-radius:19px;background:var(--gold);color:var(--white);font-size:12px;font-weight:700;line-height:38px;text-align:center}
.slider-dots{top:540px;left:512px;display:flex;gap:12px}
.slider-dots span{width:40px;height:3px;background:rgba(255,255,255,.85)}
.emblem{top:592px;left:567px;width:66px;height:66px;border-radius:50%;background:var(--white);display:flex;align-items:center;justify-content:center}
.emblem span{width:40px;height:40px;border-radius:50%;background:var(--gold)}

/* intro */
h2{font-weight:700;font-size:30px;line-height:38px;color:var(--ink)}
.intro-title{top:720px}
.intro-copy{top:826px;left:268px;width:664px;text-align:center;font-size:12.5px;line-height:24px}
.intro-copy p+p{margin-top:12px}

/* testimonial */
.band{top:980px;left:0}
.testi-title{top:1085px;color:var(--white)}
.quote{top:1160px;left:234px;width:732px;text-align:center;font-family:"Lora",Georgia,serif;font-style:italic;font-size:16.5px;line-height:31px;color:#fbf3e0}
.qmark{font-family:"Roboto Slab",Georgia,serif;font-style:normal;font-weight:700;font-size:44px;line-height:0;vertical-align:-14px;color:var(--white)}
.author{top:1338px;font-size:18px;font-weight:700;color:var(--white)}
.arrow{top:1205px}

/* clients */
.clients-title{top:1530px}
.grid{top:1606px;left:172px;display:grid;grid-template-columns:repeat(6,134px);grid-auto-rows:96px;column-gap:10px;row-gap:13px}
.tile{border:1px solid #cfcfcf;display:flex;align-items:center;justify-content:center}
.tile i{display:block;width:46px;height:46px;background:#d8d8d8}
.tile i.round{border-radius:50%}

/* signup */
.signup-bg{top:2000px;left:0}
.signup-title{top:2130px}
.signup-copy{top:2237px;left:330px;width:540px;text-align:center;font-size:12.5px;line-height:21px}
.form{top:2316px;left:220px;display:flex;gap:6px}
.field{width:249px;height:38px;border:1px solid #a9a9a9;background:#f6f6f6;font-size:13px;color:#555;padding:0 10px;line-height:36px}
.btn-download{width:249px;height:38px;background:var(--gold);color:var(--white);font-size:12px;font-weight:700;line-height:38px;text-align:center}
.signup-note{top:2402px;left:268px;width:664px;text-align:center;font-size:12.5px;line-height:21px}

/* footer */
.footer-bg{top:2470px;left:0}
.f-brand{top:2580px;left:176px;width:188px;text-align:center;color:var(--white)}
.f-brand .mark{width:82px;height:82px;border-radius:50%;border:3px solid var(--white);margin:0 auto 8px}
.f-brand .name{font-size:21px;letter-spacing:.5px}
.f-brand .tag{font-size:11px}
.f-col{top:2596px;color:var(--white)}
.f-col h3{font-weight:400;font-size:20px;margin-bottom:16px}
.f-links{left:442px;font-size:12.5px;line-height:21.6px}
.f-contact{left:607px;font-size:11.5px}
.c-row{display:flex;gap:14px;align-items:flex-start;margin-bottom:14px;line-height:19px}
.c-row svg{flex:none}
.f-follow{left:884px}
.socials{display:flex;gap:24px;margin-top:4px}
.socials span{width:20px;height:20px;border-radius:50%;background:var(--white)}
.f-rule{top:2802px;left:172px;width:856px;height:1px;background:rgba(255,255,255,.3)}
.copyright{top:2826px;font-size:11px;color:var(--white)}
</style>
</head>
<body>

<div class="abs top-line"></div>
<div class="abs brand">
  <span class="brand-dot"></span>
  <div class="brand-name">BROOKFERN ADVISORY<small>Strategy. Workshops. Coaching.</small></div>
</div>
<nav class="abs nav">
  <a class="active">HOME</a><a>ABOUT</a><a>SERVICES</a><a>ARTICLES</a><a>CONTACT</a>
</nav>

<svg class="abs hero" width="1200" height="560" role="img" aria-label="Photo of business people seated around a conference table, silhouetted against a sunset city skyline with a world map overlay">
  <defs>
    <linearGradient id="heroSky" x1="0" y1="0" x2="0" y2="1">
      <stop offset="0" stop-color="#3d8fc4"/>
      <stop offset="0.45" stop-color="#b9d3e2"/>
      <stop offset="0.65" stop-color="#f0a24a"/>
      <stop offset="0.82" stop-color="#b8402a"/>
      <stop offset="1" stop-color="#3a1c24"/>
    </linearGradient>
  </defs>
  <polygon points="0,0 1200,0 1200,531 0,555" fill="url(#heroSky)"/>
</svg>
<div class="abs center hero-title">BROOKFERN ADVISORY</div>
<div class="abs btn-start">GET STARTED</div>
<div class="abs slider-dots"><span></span><span></span><span></span><span></span></div>
<div class="abs emblem"><span></span></div>

<h2 class="abs center intro-title">Great Companies Succeed<br>by Investing in the Right People</h2>
<div class="abs intro-copy">
  <p>people for your company. And yet, knowing how to cultivate a strong staff and keep them focused on the road ahead can be challenging for even the savviest organizational leaders and human resource executives.</p>
  <p>I'm Dr. Miriam Halvorsen and I want to help business owners, leaders, and HR teams understand how to identify, develop, and retain talented professionals who can take your success to the next level.</p>
</div>

<svg class="abs band" width="1200" height="510" aria-hidden="true">
  <polygon points="0,63 1200,6 1200,440 0,503" fill="var(--gold)"/>
</svg>
<h2 class="abs center testi-title">Testimonials</h2>
<div class="abs quote"><span class="qmark">“</span> After working in the consulting business for 12 years, I met Miriam. I was immediately impressed by her ability to ask the right questions. It is rare to find someone with her credentials who also continues to have deep curiosity and creativity about their area of expertise. Miriam has a passion for helping people reach their full potential from the classroom to c-suite and Brookfern Advisory is a powerful platform to push people to their personal best. <span class="qmark">”</span></div>
<div class="abs center author">- Joan R</div>
<svg class="abs arrow" style="left:112px" width="30" height="56" aria-hidden="true"><polyline points="28,2 2,28 28,54" fill="none" stroke="#fff" stroke-width="1.5"/></svg>
<svg class="abs arrow" style="left:1090px" width="30" height="56" aria-hidden="true"><polyline points="2,2 28,28 2,54" fill="none" stroke="#fff" stroke-width="1.5"/></svg>

<h2 class="abs center clients-title">Clients &amp; Partners</h2>
<div class="abs grid" role="list" aria-label="Client and partner badges">
  <div class="tile"><i class="round"></i></div><div class="tile"><i></i></div><div class="tile"><i class="round"></i></div>
  <div class="tile"><i></i></div><div class="tile"><i></i></div><div class="tile"><i class="round"></i></div>
  <div class="tile"><i></i></div><div class="tile"><i class="round"></i></div><div class="tile"><i></i></div>
  <div class="tile"><i class="round"></i></div><div class="tile"><i></i></div><div class="tile"><i></i></div>
  <div class="tile"><i class="round"></i></div><div class="tile"><i></i></div><div class="tile"><i class="round"></i></div>
  <div class="tile"><i></i></div><div class="tile"><i></i></div><div class="tile"><i class="round"></i></div>
</div>

<svg class="abs signup-bg" width="1200" height="520" aria-hidden="true">
  <polygon points="0,71 1200,6 1200,520 0,520" fill="var(--muted)"/>
  <line x1="0" y1="71" x2="1200" y2="6" stroke="var(--gold)" stroke-width="5"/>
</svg>
<h2 class="abs center signup-title">Learn to Inspire Employees and<br>Unlock Their Maximum Potential</h2>
<div class="abs signup-copy">If you're struggling to connect with today's employees and you need to develop a better way to lead them, I want to help you become the very best leader possible.</div>
<div class="abs form">
  <div class="field">First Name</div>
  <div class="field">Email</div>
  <div class="btn-download">DOWNLOAD FREE INFORMATION</div>
</div>
<div class="abs signup-note">You'll receive monthly updates filled with leader-focused resources and helpful information that will help you build stronger organizational leaders. You can unsubscribe at any time.</div>

<svg class="abs footer-bg" width="1200" height="401" role="img" aria-label="Dimmed photo of colleagues talking in an office">
  <defs>
    <linearGradient id="footShade" x1="0" y1="0" x2="1" y2="1">
      <stop offset="0" stop-color="#5a5a5a"/>
      <stop offset="1" stop-color="#2f2f2f"/>
    </linearGradient>
  </defs>
  <polygon points="0,104 1200,5 1200,401 0,401" fill="url(#footShade)"/>
</svg>
<div class="abs f-brand">
  <div class="mark"></div>
  <div class="name">BROOKFERN ADVISORY</div>
  <div class="tag">Strategy. Workshops. Coaching.</div>
</div>
<div class="abs f-col f-links">
  <h3>Links</h3>
  <div>Home</div><div>About</div><div>Services</div><div>Articles</div><div>Contact</div>
</div>
<div class="abs f-col f-contact">
  <h3>Contact Us</h3>
  <div class="c-row">
    <svg width="18" height="24" viewBox="0 0 18 24" aria-hidden="true"><path d="M9 1C4.6 1 1 4.5 1 8.8 1 14.5 9 23 9 23s8-8.5 8-14.2C17 4.5 13.4 1 9 1z" fill="none" stroke="#fff" stroke-width="1.3"/><circle cx="9" cy="9" r="3" fill="none" stroke="#fff" stroke-width="1.3"/></svg>
    <div>Brookfern Advisory is based in<br>Georgia yet serves clients<br>nationwide.</div>
  </div>
  <div class="c-row">
    <svg width="20" height="20" viewBox="0 0 20 20" aria-hidden="true"><path d="M4 1l4 4-2.5 2.5c1.2 2.7 3.3 4.8 6 6L14 11l4 4-3 3C8 17 3 12 1 4z" fill="none" stroke="#fff" stroke-width="1.3"/></svg>
    <div>Phone: 555.014.2280</div>
  </div>
  <div class="c-row">
    <svg width="22" height="16" viewBox="0 0 22 16" aria-hidden="true"><rect x="1" y="1" width="20" height="14" fill="none" stroke="#fff" stroke-width="1.3"/><polyline points="1,1 11,9 21,1" fill="none" stroke="#fff" stroke-width="1.3"/></svg>
    <div>info@brookfernadvisory.com</div>
  </div>
</div>
<div class="abs f-col f-follow">
  <h3>Follow Us</h3>
  <div class="socials"><span></span><span></span><span></span></div>
</div>
<div class="abs f-rule"></div>
<div class="abs center copyright">© 2019 All Rights Are Reserved Terms of Use | Privacy Policy</div>

</body>
</html>
```